Industrial Company Website

We need a Website to highlight 5 different Brands we distribute.

We are Dealers for the following products

1)Velorin Tube a Div of Darvell Ostrick ( HDPE Pipes and Fittings )
Velorin Tube is the largest provider of polyethylene pipe (poly pipe) - HDPE pressure pipe and fittings in North America
Inquire page for web user to request pricing.

2) Brantock Weldline Mfg . ( HDPE Fusion Equipment )'
We like to have a system we are able to list top 25 items with part numbers and cost
that a web user is able to select and add to cart and email a order via the web.

3) Olvane Power ( Gate , Check and Globe Valves )
Sub Category Brands , Tessmark , Varilok , and Hollister Valves

4) Fertani North America Valves
http://www.fertaninorthamerica.example/ita/home.pag

5) Corlett Strainers, Inc. - A worldwide manufacturer of heavy-duty air, lube, fuel, coolant, transmission, and hydraulic filtration products
Within this Tab we like to web user to lookup filters from
http://catalog.corlettstrainer.example/ and able to create a inquire
for our company to send a quote .

6) Hargrove-Tamsin Uniforms
http://www.tamsinwear.example/
http://www.gardlyne.example/fireservice/

http://www.pelstrideboots.example/ (Safety Shoes)

Also we like a Tab for Company Profile , and contact information

We have authorization from all companies listed about to use their logo
under our dealership agreements.
Updates

Hello All ,

Please do not use the Tarvix Oil & Gas Logo.

Please Only use the Logo with the Logo with the M and the Flame and Oil Drop

Rex                                   

Target Market(s)

Target Markets ,: International distributor of pipe, valves, fittings and more
serving the Caribbean and South America .

Target Clients : Oil and Gas , Power Plants and Mining Companies

The Web Address will be www.tarvixsupply.example

Industry/Entity Type

It Company

Requirements
Must have
• Note : This Project will possibly lead to the next stage.
Coded and HTML proof of concept to load live.
I will give the winner first chance to Quote me the completion

Note the Goal is to have a E-Comm. Site , but since we are in Wholesale
and not retail . The E-Cart will no take payment but create an inquire and then send me to my email for processing
Nice to have
• I just had a Logo created by a designer on Graphic hive. I will need to share the logo design for your submission

```html
<!DOCTYPE html>
<html lang="en">
<head>
<meta charset="utf-8">
<title>Tarvix Supply – Home</title>
<link href="https://fonts.googleapis.com/css2?family=Bree+Serif&family=Open+Sans:wght@400;600&family=Roboto+Condensed:wght@400;700&display=swap" rel="stylesheet">
<style>
:root{
  --page:#efeeec;
  --white:#ffffff;
  --nav:#3a3a3a;
  --footer:#333333;
  --accent:#e0262b;
  --gold:#f3b712;
  --ink:#2b2b2b;
  --body:#3d3d3d;
  --muted:#8a8a8a;
  --frame:#d3d3d3;
  --btn:#5b5b5b;
  --foot-text:#e8e8e8;
  --foot-soft:#d6d6d6;
}
*{box-sizing:border-box;margin:0;padding:0}
html,body{width:1151px;height:1200px;overflow:hidden}
body{position:relative;background:var(--page);font-family:"Open Sans",sans-serif;color:var(--body)}
.abs{position:absolute}
.header{left:0;top:0;width:1151px;height:110px;background:var(--white)}
.brand-mark{left:135px;top:14px;width:144px;height:96px;display:flex;flex-direction:column;align-items:center;justify-content:center;gap:8px}
.brand-mark .dot{width:44px;height:44px;border-radius:50%;background:var(--gold)}
.brand-mark .name{font-size:8px;font-weight:600;color:var(--nav);text-align:center;line-height:1.2}
.callus{left:843px;top:24px;display:flex;align-items:center;gap:6px}
.callus .label{font-size:12px;color:var(--ink)}
.callus .number{font-size:20px;color:var(--ink);line-height:1}
.navbar{left:0;top:110px;width:1151px;height:36px;background:var(--nav)}
.nav-logo-foot{left:135px;top:110px;width:144px;height:36px;background:var(--white)}
.nav{left:331px;top:110px;display:flex;height:36px;font-family:"Bree Serif",serif;font-size:14px}
.nav a{color:var(--white);text-decoration:none;display:flex;align-items:center;justify-content:center;height:36px;position:relative}
.nav a+a::before{content:"";position:absolute;left:0;top:11px;height:15px;border-left:1px solid #5a5a5a}
.nav a.active{background:var(--white);color:var(--accent);border-top:4px solid var(--gold)}
.nav a.active::before{display:none}
.nav a.active+a::before{display:none}
.slider{left:135px;top:168px;width:881px;height:323px;background:var(--frame)}
.slide{left:144px;top:177px;width:863px;height:304px;background:linear-gradient(180deg,#7fa8d8 0%,#a5c3e6 60%,#8b8577 100%)}
.caption{left:144px;top:445px;width:863px;height:36px;background:rgba(40,40,40,.75);color:var(--white);font-family:"Roboto Condensed",sans-serif;font-size:24px;line-height:36px;padding-left:28px;white-space:nowrap}
.arrow{width:28px;height:28px;border-radius:50%;background:var(--white);display:flex;align-items:center;justify-content:center;box-shadow:0 1px 3px rgba(0,0,0,.3)}
.section-title{left:0;width:1151px;display:flex;align-items:center;justify-content:center;gap:20px;font-size:25px;color:var(--ink);letter-spacing:.5px}
.section-title .rule{width:200px;border-top:1px solid #c4c4c4;border-bottom:1px solid #c4c4c4;height:3px}
.about-text{left:135px;top:559px;width:881px;font-size:12.8px;line-height:21.6px;text-align:center;color:var(--body)}
.brand-card{top:732px;width:162px;height:205px;background:var(--white);box-shadow:0 0 3px rgba(0,0,0,.15)}
.brand-card .logo{height:58px;display:flex;align-items:center;justify-content:center;font-size:17px;font-weight:600;color:var(--ink);text-align:center;line-height:1.1}
.brand-card .photo{margin:0 5px;height:142px;border:1px solid #ddd}
.view-all{top:937px;width:69px;height:21px;background:var(--btn);color:var(--white);font:600 12px Arial,sans-serif;display:flex;align-items:center;justify-content:center}
.footer-line{left:0;top:1003px;width:1151px;height:5px;background:var(--accent)}
.footer{left:0;top:1008px;width:1151px;height:192px;background:var(--footer)}
.quick,.contact,.newsletter{color:var(--foot-text)}
.foot-head{font-family:"Roboto Condensed",sans-serif;font-size:19px;color:var(--white);padding-bottom:6px;border-bottom:1px dotted #555}
.quick{left:138px;top:1020px;width:104px}
.quick ul{list-style:none;margin-top:10px;font-size:11px}
.quick li{height:20px;padding-left:10px;position:relative;color:var(--foot-text)}
.quick li::before{content:"›";position:absolute;left:0;top:-2px;color:#aaa}
.contact{left:299px;top:1020px;width:223px}
.contact .row{display:flex;gap:14px;font-size:11px;line-height:15px;margin-top:12px;color:var(--foot-text)}
.contact .row svg{flex:none}
.newsletter{left:578px;top:1020px;width:213px}
.newsletter p{font-size:11px;line-height:17px;margin-top:12px;color:var(--foot-text)}
.newsletter .email{margin-top:12px;width:199px;height:24px;background:var(--white);color:var(--muted);font-size:10px;line-height:24px;padding-left:8px}
.newsletter .submit{margin-top:12px;width:60px;height:24px;background:#222;border:1px solid #666;color:var(--white);font:700 12px Arial,sans-serif;display:flex;align-items:center;justify-content:center}
.vdiv{top:1020px;height:160px;border-left:1px dotted #4a4a4a}
.foot-brand{left:830px;top:1030px;width:180px;display:flex;flex-direction:column;align-items:center;gap:8px}
.foot-brand .dot{width:70px;height:70px;border-radius:50%;border:2px solid #777}
.foot-brand .name{font-size:12px;color:#aaa}
.copyright{left:820px;top:1144px;width:200px;font-size:11px;text-align:center;line-height:15px;color:var(--foot-soft)}
</style>
</head>
<body>
<header class="abs header"></header>
<div class="abs navbar"></div>
<div class="abs nav-logo-foot"></div>
<div class="abs brand-mark">
  <span class="dot"></span>
  <span class="name">HARBOR CONTINENTAL<br>MACHINERY &amp; EQUIPMENT CORP.</span>
</div>
<div class="abs callus">
  <svg width="32" height="32" viewBox="0 0 32 32"><circle cx="16" cy="16" r="14" fill="none" stroke="#e0262b" stroke-width="2"/><path d="M11 9c-2 2-1 6 2 10s7 6 9 4l-3-3-2 1c-1-1-3-3-4-5l1-2z" fill="#e0262b"/></svg>
  <div><div class="label">Call Us</div><div class="number">123 456 7890</div></div>
</div>
<nav class="abs nav">
  <a class="active" style="width:95px">Home</a>
  <a style="width:115px">About Us</a>
  <a style="width:122px">Products</a>
  <a style="width:97px">News</a>
  <a style="width:127px">Services</a>
  <a style="width:136px">Contact Us</a>
</nav>

<div class="abs slider"></div>
<div class="abs slide" role="img" aria-label="Oil field pump jacks under a blue sky with a worker in a red hard hat"></div>
<div class="abs caption">Tarvix is providing procurement &amp; service for the oil &amp; gas industries Globally</div>
<div class="abs arrow" style="left:134px;top:315px"><svg width="16" height="14" viewBox="0 0 16 14"><path d="M15 7H3M8 1 2 7l6 6" fill="none" stroke="#222" stroke-width="2.5"/></svg></div>
<div class="abs arrow" style="left:988px;top:315px"><svg width="16" height="14" viewBox="0 0 16 14"><path d="M1 7h12M8 1l6 6-6 6" fill="none" stroke="#e0262b" stroke-width="2.5"/></svg></div>

<h2 class="abs section-title" style="top:514px;font-weight:400"><span class="rule"></span>About Company<span class="rule"></span></h2>
<p class="abs about-text">Lorem ipsum dolor sit amet, consectetuer adipiscing elit, sed diam nonummy nibh euismod tincidunt ut laoreet dolore magna aliquam erat volutpat. Ut wisi enim ad minim veniam, quis nostrud exerci tation ullamcorper suscipit lobortis nisl ut aliquip ex ea commodo consequat. Duis autem vel eum iriure dolor in hendrerit in vulputate velit esse molestie consequat, vel illum dolore eu feugiat nulla facilisis at vero eros et accumsan et iusto odio dignissim qui blandit praesent luptatum zzril delenit augue duis dolore te feugait nulla facilisi.</p>

<h2 class="abs section-title" style="top:675px;font-weight:400"><span class="rule" style="width:225px"></span>Brands We Distribute<span class="rule" style="width:225px"></span></h2>

<div class="abs brand-card" style="left:135px"><div class="logo">Velorin Tube</div><div class="photo" role="img" aria-label="Stainless pipe bends on a white sheet" style="background:linear-gradient(#d9d9d6,#9a9994)"></div></div>
<div class="abs brand-card" style="left:315px"><div class="logo">Brantock</div><div class="photo" role="img" aria-label="Green tracked pipe fusion machine" style="background:linear-gradient(#f4f4f2,#3f9a5c)"></div></div>
<div class="abs brand-card" style="left:495px"><div class="logo">Olvane</div><div class="photo" role="img" aria-label="Group of industrial gate and globe valves" style="background:linear-gradient(#f7f7f7,#8c8c8c)"></div></div>
<div class="abs brand-card" style="left:676px"><div class="logo" style="font-size:13px">Fertani<br>North America, Inc.</div><div class="photo" role="img" aria-label="Blue electric actuator on a brass ball valve" style="background:linear-gradient(#b9d8ee,#3b7cc2)"></div></div>
<div class="abs brand-card" style="left:857px"><div class="logo" style="font-size:15px">Corlett Strainers</div><div class="photo" role="img" aria-label="Assorted red and silver filter canisters" style="background:linear-gradient(#f2f2f2,#c53d36)"></div></div>

<div class="abs view-all" style="left:186px">View all</div>
<div class="abs view-all" style="left:365px">View all</div>
<div class="abs view-all" style="left:546px">View all</div>
<div class="abs view-all" style="left:728px">View all</div>
<div class="abs view-all" style="left:907px">View all</div>

<div class="abs footer-line"></div>
<footer class="abs footer"></footer>
<div class="abs quick">
  <div class="foot-head">Quick Links</div>
  <ul><li>Home</li><li>About Us</li><li>Products</li><li>News</li><li>Services</li><li>Contact Us</li></ul>
</div>
<div class="abs vdiv" style="left:268px"></div>
<div class="abs contact">
  <div class="foot-head">Contact Information</div>
  <div class="row"><svg width="12" height="16" viewBox="0 0 12 16"><path d="M6 0a6 6 0 0 0-6 6c0 4 6 10 6 10s6-6 6-10a6 6 0 0 0-6-6zm0 8.5A2.5 2.5 0 1 1 6 3.5a2.5 2.5 0 0 1 0 5z" fill="#eee"/></svg><span>4120 S.W. 58th Ave, Coral Point, Florida 33012</span></div>
  <div class="row"><svg width="12" height="14" viewBox="0 0 12 14"><path d="M2 1c-2 2-1 6 2 9s6 4 7 2l-2-3-2 1C6 9 4 7 3 5l1-2z" fill="#eee"/></svg><span>Tel: 555.214.3307 /&nbsp;&nbsp; 555.214.3308</span></div>
  <div class="row" style="margin-top:18px"><svg width="16" height="14" viewBox="0 0 16 14"><rect x="4" y="0" width="8" height="4" fill="#eee"/><rect x="0" y="4" width="16" height="6" rx="1" fill="#eee"/><rect x="4" y="8" width="8" height="6" fill="#eee" stroke="#333"/></svg><span>Fax: 555.214.3309</span></div>
  <div class="row" style="margin-top:20px"><svg width="16" height="12" viewBox="0 0 16 12"><rect width="16" height="12" fill="#eee"/><path d="M0 0l8 7 8-7" fill="none" stroke="#333" stroke-width="1.5"/></svg><span>info@tarvixsupply.example</span></div>
</div>
<div class="abs vdiv" style="left:548px"></div>
<div class="abs newsletter">
  <div class="foot-head">Newsletter Signup</div>
  <p>Get the latest updates by entering your email address</p>
  <div class="email">Email Address</div>
  <div class="submit">SUBMIT</div>
</div>
<div class="abs vdiv" style="left:810px"></div>
<div class="abs foot-brand"><span class="dot"></span><span class="name">Harbor Continental</span></div>
<div class="abs copyright">Copyright © 2013 Tarvixsupply.<br>All Rights Reserved</div>
</body>
</html>
```